Postcard designed to acquire new customers

Need a postcard style AD to place in dentist offices and other professionals to promote our tax saving system. We will place these in dentists offices, orthodontist, optometrist, physiotherapist and all sorts of medical/dental offices. The card should highlight how they can save taxes by using our software. Our website has good information on it, and I'll include the advertising PDF that our software company produces. Our logo is a little out-dated and I've included the bonus of the winner re-making the logo so its better than it currently is.
Updates

I don't need to have any space allocated for a stamp and address. We are using this to place in offices and are for advertising purposes, not mailing. Thanks!

Reason: My apologies for not providing feedback yet, I've lost several days due to some illness and am finally back at work. I'll be going through designs today and would like the extra few days to work with many of you to create a great design. Thank you for your patience! Doyle

Reason: Again, my apologies for the delay. I will be in contact with designers this week. Thank you,

Target Market(s)

Small Business Owners in Canada

Industry/Entity Type

Health Insurance

Logo Text

Save Time, Save Money

Font styles to use
Other font styles liked:
• Easy to Read Font's

Colors

Designer to choose colors to be used in the design.

Requirements
Must have
• Must have a call to action on the postcard to sell the service. We need people to have their attention caught. A call to action could be, "You're spending too much on taxes! That's what they'll say if your business doesn't have a 789 Brookvale Outlay Plan..."
• See the PDF for other catch phrases or key information on what a Health Spending Account is. Many people don't know so I'd like to see 3-4 bullet points on the front of the postcard on what a health spending account is. See the attached PDF for that information and simplifying the information to short bullet points would be best. Here are my thoughts:
• Who should have a 789 Brookvale Outlay Plan?
• - Every business owner who is incorporated should have one.
• - Write off 100% of this QTB approved this method.
• - It is the most tax effective way to run dental, health, vision and other expenses through your company.
• - Easy to use APP for your phone, 2-day turnaround time for claims
• If you aren't using this, you're throwing tax dollars away!
• The back of the postcard would include 2 things. First, an example of the taxes you can save, and second - the different information they can send us so we can setup your account.
• First is the example of how this saves you money. Assuming a 38% personal tax rate. You will need to earn $1.62 of gross income, pay $0.62 of personal tax, which leaves you with $1.00 of after tax money to use for your personal expenses.
• The example of using a 789 Brookvale Outlay Plan, or doing nothing would need the following information.
• Comparison
• $5,000 of medical, dental, vision expenses
• Do Nothing 789 Brookvale Outlay Plan
• $8,100 – Total Cost $5,525 – Total Cost
• $3,100 – Income Tax $500 fee & $25 GST
• $5,000 – Money needed for medical, dental, vision, etc. $5,000 – Money needed for medical, dental, vision, etc.
• SAVINGS is $2,575
• Assuming a company incorporated in Alberta and a one time setup fee of $275 has not been included in the comparison.
• Information to send us to setup your account is:
• - Names and birth dates of you and your dependents
• - Contact information for you and your business (if different) Address, email, phone numbers
• - We will contact you about how to setup the app, your banking details and some other items.
• - Setup fee is a one-time payment of $275
Nice to have
• I'd like the front of the postcard to not be very busy with the background or graphics, etc. I want the call to action to be very obvious so they want to read the bullet points and look at the back of the postcard for more information.

```html
<!DOCTYPE html>
<html lang="en">
<head>
<meta charset="utf-8">
<title>789 Brookvale Outlay Plan – Postcard</title>
<link href="https://fonts.googleapis.com/css2?family=Exo+2:wght@500;600;800&family=Ropa+Sans&family=Roboto:wght@300;400;700&family=Roboto+Condensed:wght@400;700&display=swap" rel="stylesheet">
<style>
:root{
  --ink:#2a2a2a;
  --ink-deep:#1d1d1d;
  --yellow:#f7b618;
  --orange:#f47b20;
  --white:#ffffff;
  --page:#e9e9e9;
  --muted:#e8e8e8;
}
*{box-sizing:border-box;margin:0;padding:0}
html,body{width:891px;height:1200px;overflow:hidden;background:var(--page)}
.card{position:absolute;left:51px;width:789px;height:510px;overflow:hidden;box-shadow:0 6px 16px rgba(0,0,0,.25)}
.card--front{top:40px;background:var(--white)}
.card--back{top:630px}
.shapes{position:absolute;inset:0}
.layer{position:absolute}

/* front */
.brand{left:170px;top:26px;display:flex;align-items:center;gap:8px;font-family:"Exo 2",sans-serif;font-weight:800;font-size:15px;color:var(--ink);letter-spacing:.3px}
.brand__mark{width:22px;height:22px;background:var(--yellow)}
.hook{left:12px;top:95px;width:503px;height:148px;border:1px dashed var(--orange);border-radius:6px;text-align:center;font-family:"Exo 2",sans-serif;color:var(--white);padding-top:7px}
.hook__lead{font-weight:500;font-size:24px;line-height:23.5px;letter-spacing:.9px}
.hook__name{font-weight:800;font-size:28px;line-height:31px;color:var(--yellow);margin-top:6px;text-transform:uppercase;letter-spacing:1px}
.who{left:12px;top:273px;width:503px;height:36px;border:1px dashed var(--ink);border-radius:5px;font-family:"Ropa Sans",sans-serif;font-size:25px;line-height:32px;color:var(--ink);padding-left:10px;white-space:nowrap}
.points{left:14px;top:320px;width:480px;list-style:none;font-family:"Ropa Sans",sans-serif;font-size:17.5px;line-height:19px;color:var(--ink)}
.points li{position:relative;padding-left:20px;margin-bottom:6.5px}
.points li svg{position:absolute;left:0;top:3px}
.expert{right:16px;top:390px;font-family:"Ropa Sans",sans-serif;font-size:15.5px;color:var(--yellow);text-transform:uppercase;letter-spacing:.3px}
.phone{right:16px;top:404px;font-family:"Roboto Condensed",sans-serif;font-weight:700;font-size:40px;color:var(--white);letter-spacing:.5px}
.visit{left:648px;top:452px;width:126px;height:17px;border-radius:9px;background:var(--white);font-family:"Roboto Condensed",sans-serif;font-size:13px;line-height:17px;text-align:center;color:var(--ink)}
.web{right:16px;top:472px;display:flex;align-items:center;gap:6px;font-family:"Ropa Sans",sans-serif;font-size:20px;color:var(--white);letter-spacing:.5px}

/* back */
.tab{font-family:"Ropa Sans",sans-serif;font-size:19.5px;color:var(--ink);text-transform:uppercase}
.tab span{display:inline-block;border:1px dashed var(--ink);border-radius:4px;padding:2px 6px}
.tab--example{left:12px;top:17px}
.tab--setup{left:12px;top:346px}
.body{font-family:"Roboto",sans-serif;font-weight:300;font-size:12.6px;line-height:14.5px;color:var(--muted)}
.intro{left:18px;top:64px;width:608px;line-height:15.8px}
.note{left:18px;top:117px;width:530px;font-family:"Ropa Sans",sans-serif;font-size:13.8px;line-height:16px;color:var(--yellow)}
.list{list-style:none}
.list li{position:relative;padding-left:17px;margin-bottom:4px}
.list li svg{position:absolute;left:0;top:2px}
.list--compare{left:14px;top:155px;width:500px}
.list--setup{left:14px;top:394px;width:470px}
.list--setup li{margin-bottom:5px}
.hi{color:var(--yellow);font-weight:400}
.strong{font-weight:700;color:var(--white)}
.slot{position:absolute;background:var(--white);font-family:"Roboto Condensed",sans-serif;font-size:13.5px;color:#111;text-align:center}
.slot--postage{left:660px;top:13px;width:116px;height:115px;padding-top:45px;line-height:22px}
.slot--address{left:523px;top:224px;width:253px;height:275px;padding-top:49px}
.slot--barcode{left:340px;top:441px;width:436px;height:58px;padding-top:26px}
</style>
</head>
<body>

<section class="card card--front" aria-label="Postcard front">
  <svg class="shapes" width="789" height="510" viewBox="0 0 789 510">
    <defs>
      <linearGradient id="officeTone" x1="0" y1="0" x2="0" y2="1">
        <stop offset="0" stop-color="#3a3a3c"/>
        <stop offset=".55" stop-color="#6b6e72"/>
        <stop offset="1" stop-color="#2a2a2b"/>
      </linearGradient>
      <clipPath id="innerArea"><path d="M0 0H508C598 90 616 300 523 510H0Z"/></clipPath>
    </defs>
    <rect width="789" height="510" fill="url(#officeTone)" role="img" aria-label="Photo: two businessmen by a high office window overlooking a city"/>
    <path d="M0 0H522C614 90 634 300 542 510H0Z" fill="var(--yellow)"/>
    <path d="M0 0H508C598 90 616 300 523 510H0Z" fill="var(--ink)"/>
    <path d="M0 0H486C568 100 584 300 488 510H0Z" fill="var(--white)"/>
    <g clip-path="url(#innerArea)">
      <rect x="0" y="85" width="640" height="182" fill="var(--ink)"/>
      <rect x="0" y="267" width="640" height="43" fill="var(--yellow)"/>
    </g>
    <path d="M292 252H308L300 259Z" fill="var(--ink)"/>
    <path d="M292 310H308L300 317Z" fill="var(--yellow)"/>
    <rect x="537" y="383" width="252" height="81" fill="var(--ink-deep)"/>
    <rect x="0" y="498" width="789" height="12" fill="var(--yellow)"/>
    <rect x="510" y="464" width="279" height="46" fill="var(--orange)"/>
  </svg>

  <div class="layer brand"><span class="brand__mark"></span>789 BROOKVALE OUTLAY</div>

  <div class="layer hook">
    <p class="hook__lead">You're spending too much on taxes!<br>That's what they'll say if your<br>business doesn't have a</p>
    <p class="hook__name">789 Brookvale Outlay<br>Plan...</p>
  </div>

  <div class="layer who">Who should have a 789 Brookvale Outlay Plan?</div>

  <ul class="layer points">
    <li><svg width="14" height="14" viewBox="0 0 14 14"><circle cx="7" cy="7" r="7" fill="var(--yellow)"/><path d="M5.5 4l3 3-3 3" stroke="#fff" stroke-width="1.8" fill="none"/></svg>Every business owner who is incorporated should have one.</li>
    <li><svg width="14" height="14" viewBox="0 0 14 14"><circle cx="7" cy="7" r="7" fill="var(--yellow)"/><path d="M5.5 4l3 3-3 3" stroke="#fff" stroke-width="1.8" fill="none"/></svg>Write off 100% of this QTB approved this method.</li>
    <li><svg width="14" height="14" viewBox="0 0 14 14"><circle cx="7" cy="7" r="7" fill="var(--yellow)"/><path d="M5.5 4l3 3-3 3" stroke="#fff" stroke-width="1.8" fill="none"/></svg>It is the most tax effective way to run dental, health,<br>vision and other expenses through your company.</li>
    <li><svg width="14" height="14" viewBox="0 0 14 14"><circle cx="7" cy="7" r="7" fill="var(--yellow)"/><path d="M5.5 4l3 3-3 3" stroke="#fff" stroke-width="1.8" fill="none"/></svg>Easy to use APP for your phone, 2-day turnaround time<br>for claims</li>
    <li><svg width="14" height="14" viewBox="0 0 14 14"><circle cx="7" cy="7" r="7" fill="var(--yellow)"/><path d="M5.5 4l3 3-3 3" stroke="#fff" stroke-width="1.8" fill="none"/></svg>If you aren't using this, you're throwing tax dollars away!</li>
  </ul>

  <div class="layer expert">Speak with our expert:</div>
  <div class="layer phone">0155 204 718</div>
  <div class="layer visit">Visit our Website</div>
  <div class="layer web"><svg width="15" height="15" viewBox="0 0 16 16" fill="none" stroke="#fff" stroke-width="1.3"><circle cx="8" cy="8" r="7"/><ellipse cx="8" cy="8" rx="3" ry="7"/><path d="M1 8h14M2.5 4.5h11M2.5 11.5h11"/></svg>www.brookvaleoutlay.ca</div>
</section>

<section class="card card--back" aria-label="Postcard back">
  <svg class="shapes" width="789" height="510" viewBox="0 0 789 510">
    <defs>
      <linearGradient id="skylineTone" x1="0" y1="0" x2="0" y2="1">
        <stop offset="0" stop-color="#3c3b3a"/>
        <stop offset=".6" stop-color="#2c2d30"/>
        <stop offset="1" stop-color="#1c1d20"/>
      </linearGradient>
    </defs>
    <rect width="789" height="510" fill="url(#skylineTone)" role="img" aria-label="Photo: dusky city skyline with tall towers"/>
    <path d="M0 14H409L396 48H0Z" fill="var(--yellow)"/>
    <path d="M204 48H220L212 55Z" fill="var(--yellow)"/>
    <path d="M0 344H499L486 378H0Z" fill="var(--yellow)"/>
    <path d="M204 378H220L212 385Z" fill="var(--yellow)"/>
  </svg>

  <div class="layer tab tab--example"><span>An example of the taxes you can save</span></div>

  <p class="layer body intro">First is the example of how this saves you money. Assuming a 38% personal tax rate. You will need to earn $1.62 of gross income, pay $0.62 of personal tax, which leaves you with $1.00 of after tax money to use for your personal expenses.</p>

  <p class="layer note">The example of using a 789 Brookvale Outlay Plan, or doing nothing would need the following information.</p>

  <ul class="layer body list list--compare">
    <li><svg width="11" height="11" viewBox="0 0 14 14"><circle cx="7" cy="7" r="7" fill="var(--yellow)"/><path d="M5.5 4l3 3-3 3" stroke="#222" stroke-width="2" fill="none"/></svg>Comparison</li>
    <li><svg width="11" height="11" viewBox="0 0 14 14"><circle cx="7" cy="7" r="7" fill="var(--yellow)"/><path d="M5.5 4l3 3-3 3" stroke="#222" stroke-width="2" fill="none"/></svg><span class="hi">$5,000</span> of medical, dental, vision expenses</li>
    <li><svg width="11" height="11" viewBox="0 0 14 14"><circle cx="7" cy="7" r="7" fill="var(--yellow)"/><path d="M5.5 4l3 3-3 3" stroke="#222" stroke-width="2" fill="none"/></svg>Do Nothing&nbsp;&nbsp;789 Brookvale Outlay Plan</li>
    <li><svg width="11" height="11" viewBox="0 0 14 14"><circle cx="7" cy="7" r="7" fill="var(--yellow)"/><path d="M5.5 4l3 3-3 3" stroke="#222" stroke-width="2" fill="none"/></svg><span class="hi">$8,100</span> <span class="strong">– Total Cost</span>&nbsp;&nbsp;<span class="hi">$5,525</span> <span class="strong">– Total Cost</span></li>
    <li><svg width="11" height="11" viewBox="0 0 14 14"><circle cx="7" cy="7" r="7" fill="var(--yellow)"/><path d="M5.5 4l3 3-3 3" stroke="#222" stroke-width="2" fill="none"/></svg><span class="hi">$3,100</span> – Income Tax <span class="hi">$500</span> fee &amp; <span class="hi">$25 GST</span></li>
    <li><svg width="11" height="11" viewBox="0 0 14 14"><circle cx="7" cy="7" r="7" fill="var(--yellow)"/><path d="M5.5 4l3 3-3 3" stroke="#222" stroke-width="2" fill="none"/></svg><span class="hi">$5,000</span> – Money needed for medical, dental, vision, etc.&nbsp;&nbsp;<span class="hi">$5,000</span> – Money needed for medical, dental, vision, etc.</li>
    <li><svg width="11" height="11" viewBox="0 0 14 14"><circle cx="7" cy="7" r="7" fill="var(--yellow)"/><path d="M5.5 4l3 3-3 3" stroke="#222" stroke-width="2" fill="none"/></svg>SAVINGS is <span class="hi">$2,575</span></li>
    <li><svg width="11" height="11" viewBox="0 0 14 14"><circle cx="7" cy="7" r="7" fill="var(--yellow)"/><path d="M5.5 4l3 3-3 3" stroke="#222" stroke-width="2" fill="none"/></svg>Assuming a company incorporated in Alberta and a one time setup fee of <span class="hi">$275</span> has not been included in the comparison.</li>
  </ul>

  <div class="layer tab tab--setup"><span>Information to send us to setup your account is</span></div>

  <ul class="layer body list list--setup">
    <li><svg width="11" height="11" viewBox="0 0 14 14"><circle cx="7" cy="7" r="7" fill="var(--yellow)"/><path d="M5.5 4l3 3-3 3" stroke="#222" stroke-width="2" fill="none"/></svg>Names and birth dates of you and your dependents</li>
    <li><svg width="11" height="11" viewBox="0 0 14 14"><circle cx="7" cy="7" r="7" fill="var(--yellow)"/><path d="M5.5 4l3 3-3 3" stroke="#222" stroke-width="2" fill="none"/></svg>Contact information for you and your business (if different) Address, email, phone numbers</li>
    <li style="width:310px"><svg width="11" height="11" viewBox="0 0 14 14"><circle cx="7" cy="7" r="7" fill="var(--yellow)"/><path d="M5.5 4l3 3-3 3" stroke="#222" stroke-width="2" fill="none"/></svg>We will contact you about how to setup the app, your banking details and some other items.</li>
    <li><svg width="11" height="11" viewBox="0 0 14 14"><circle cx="7" cy="7" r="7" fill="var(--yellow)"/><path d="M5.5 4l3 3-3 3" stroke="#222" stroke-width="2" fill="none"/></svg>Setup fee is a one-time payment of <span class="hi">$275</span></li>
  </ul>

  <div class="slot slot--postage">Postage<br>Area</div>
  <div class="slot slot--address">Address Area</div>
  <div class="slot slot--barcode">Barcode Area</div>
</section>

</body>
</html>
```